Brennick - Business Card Design

Design a modern masculine business card for our business

Target Market(s)

Private Market

Industry/Entity Type

Construction

Contact Information for Business Card

Company Name - Name of Person - Address - email address - contact number

Font styles to use
Serif
Sans Serif

Colors
0094D4
00A9DD
6FCCEA
C7EBF8
E9F6FB
00AB8E
00BBA5
67D7C9
C6EFE9
E9F9F6
F0912C
F2A743
F7CA91
FBE8D2
FDF5EE

Requirements
Must have
• Use company logo provided
Nice to have
• Company Logo

```html
<!DOCTYPE html>
<html lang="en">
<head>
<meta charset="utf-8">
<title>Brennick Construction – Business Card</title>
<link href="https://fonts.googleapis.com/css2?family=Lato:wght@400;700;900&display=swap" rel="stylesheet">
<style>
  :root{
    --stage:#3a3a3a;
    --card-black:#111111;
    --card-white:#ffffff;
    --orange:#f2732b;
    --ink:#111111;
    --paper:#ffffff;
  }
  *{margin:0;padding:0;box-sizing:border-box}
  html,body{width:1200px;height:689px;overflow:hidden}
  body{background:var(--stage);font-family:"Lato",Arial,sans-serif;position:relative}
  .card{position:absolute;width:520px;height:297px;top:196px;overflow:hidden;box-shadow:0 14px 30px rgba(0,0,0,.45)}
  .card--front{left:50px;background:var(--card-black);display:flex;align-items:center;justify-content:center}
  .card--back{left:630px;background:var(--card-white)}
  .brand{display:flex;align-items:center;gap:14px}
  .brand__mark{width:22px;height:22px;background:var(--orange);flex:none}
  .brand__name{font-weight:900;text-transform:uppercase;line-height:1.05}
  .card--front .brand__name{color:var(--paper);font-size:34px;letter-spacing:1px}
  .card--back .brand{position:absolute;left:30px;bottom:36px;gap:10px}
  .card--back .brand__mark{width:14px;height:14px}
  .card--back .brand__name{color:var(--ink);font-size:18px;letter-spacing:.5px}
  .back-art{position:absolute;inset:0}
  .contact{position:absolute;top:16px;right:20px;text-align:right;color:var(--paper)}
  .contact__name{font-size:22px;font-weight:900;text-transform:uppercase;letter-spacing:.5px;line-height:1.1}
  .contact__title{font-size:13px;margin-bottom:5px}
  .contact__list{list-style:none;font-size:10.5px;line-height:14px}
  .contact__list li{display:flex;justify-content:flex-end;align-items:center;gap:6px}
  .contact__list .no-icon{padding-right:16px}
  .icon{width:10px;height:10px;flex:none}
</style>
</head>
<body>
  <section class="card card--front">
    <div class="brand">
      <span class="brand__mark"></span>
      <span class="brand__name">Brennick<br>Construction, Inc</span>
    </div>
  </section>

  <section class="card card--back">
    <svg class="back-art" width="520" height="297" viewBox="0 0 520 297">
      <polygon points="0,0 520,0 520,220 0,30" fill="var(--orange)"/>
      <line x1="90" y1="75" x2="505" y2="226.5" stroke="var(--ink)" stroke-width="3"/>
      <line x1="330" y1="172.6" x2="500" y2="234.7" stroke="var(--orange)" stroke-width="4"/>
    </svg>

    <div class="contact">
      <div class="contact__name">Marcus Hale</div>
      <div class="contact__title">Founder &amp; CEO</div>
      <ul class="contact__list">
        <li>Your Address, City
          <svg class="icon" viewBox="0 0 10 10"><path d="M5 0a3.5 3.5 0 0 0-3.5 3.5C1.5 6 5 10 5 10s3.5-4 3.5-6.5A3.5 3.5 0 0 0 5 0z" fill="#fff"/><circle cx="5" cy="3.5" r="1.3" fill="var(--orange)"/></svg></li>
        <li class="no-icon">State, Zip 1235</li>
        <li>(123) 456-7890
          <svg class="icon" viewBox="0 0 10 10"><path d="M2 0.5l2 2-1 1.2c.6 1.3 1.6 2.3 2.9 2.9L7 5.6l2 2-1.2 1.6C4 9 1 6 .8 2z" fill="#fff"/></svg></li>
        <li>(231) 456-7890
          <svg class="icon" viewBox="0 0 10 10"><rect x="2.5" y="0.5" width="5" height="9" rx="1" fill="none" stroke="#fff"/><circle cx="5" cy="8" r=".6" fill="#fff"/></svg></li>
        <li>(312) 456-7890
          <svg class="icon" viewBox="0 0 10 10"><rect x="1" y="4" width="8" height="5" fill="#fff"/><rect x="2.5" y="1" width="5" height="3" fill="none" stroke="#fff"/></svg></li>
        <li>info@yourwebsite.com
          <svg class="icon" viewBox="0 0 10 10"><rect x="0.5" y="2" width="9" height="6.5" fill="#fff"/><path d="M.5 2l4.5 3.5L9.5 2" fill="none" stroke="var(--orange)"/></svg></li>
        <li>yourwebsite.com
          <svg class="icon" viewBox="0 0 10 10"><circle cx="5" cy="5" r="4.5" fill="#fff"/><path d="M.5 5h9M5 .5c-2 2.5-2 6.5 0 9M5 .5c2 2.5 2 6.5 0 9" fill="none" stroke="var(--orange)" stroke-width=".7"/></svg></li>
      </ul>
    </div>

    <div class="brand">
      <span class="brand__mark"></span>
      <span class="brand__name">Brennick<br>Construction, Inc</span>
    </div>
  </section>
</body>
</html>
```